Steadway Halvicor

We're designing a website to sell Halvicor Supplements. Attached is an image of the words we want to say and general layout, but please use your best knowledge to make it better. This platform is intentionally simplistic because this is reaching an older demographic, so it should be very straightforward, attention-grabbing and extremely user-friendly, while still appearing reliable and professional.
Use your best judgement for color palate that conveys professional but approachable. Feel free to add imagery but don't overwhelm the page.
Updates
Designs look the same
Target Market(s)
65+ seniors
Number of Pages Required
1 page
Look and feel

```html
<!DOCTYPE html>
<html lang="en">
<head>
<meta charset="utf-8">
<title>Steadway Halvicor</title>
<link href="https://fonts.googleapis.com/css2?family=Open+Sans:wght@400;600;700;800&family=Oswald:wght@500;700&display=swap" rel="stylesheet">
<style>
:root{
  --blue:#1b8fd8;
  --blue-dark:#0f6fb0;
  --navy:#1d3e6e;
  --red:#e1262d;
  --ink:#333;
  --muted:#888;
  --line:#e4e4e4;
  --soft:#f4f6f8;
  --footer:#141414;
  --canvas:#e9e9e9;
}
*{box-sizing:border-box;margin:0;padding:0}
html,body{width:809px;height:1200px;overflow:hidden;background:var(--canvas);font-family:"Open Sans",sans-serif;color:var(--ink)}
.board{position:relative;width:809px;height:1200px}
.page{position:absolute;top:6px;width:392px;height:1188px;background:#fff;overflow:hidden}
.page--home{left:6px}
.page--quote{left:411px}

.site-header{height:28px;display:flex;align-items:center;justify-content:space-between;padding:0 12px}
.brand{display:flex;align-items:center;gap:4px;font-weight:800;font-size:7px;color:var(--red);text-transform:uppercase}
.brand-dot{width:8px;height:8px;border-radius:50%;background:var(--blue)}
.nav{display:flex;gap:8px;font-size:4.5px;color:var(--ink)}
.nav .is-active{color:var(--blue);font-weight:700}
.header-phone{font-size:6px;font-weight:700;color:var(--red)}

.hero{position:relative;height:172px;background:linear-gradient(120deg,#c9d7e2 0%,#e9eef2 45%,#b9c5cc 75%,#8c9aa0 100%)}
.hero-copy{position:absolute;left:22px;top:40px}
.hero-title{font-family:"Oswald",sans-serif;font-weight:700;font-size:24px;line-height:1;color:#fff;text-transform:uppercase;text-shadow:0 1px 2px rgba(0,0,0,.15)}
.hero-title span{color:var(--blue)}
.hero-sub{margin-top:8px;font-size:5px;color:var(--navy);width:160px}
.hero-actions{margin-top:10px;display:flex;gap:6px}
.btn{display:inline-block;padding:5px 10px;font-size:5px;font-weight:700;color:#fff;text-transform:uppercase;border-radius:2px}
.btn--red{background:var(--red)}
.btn--blue{background:var(--blue)}

.feature-strip{height:28px;background:var(--blue);display:flex;align-items:center;justify-content:space-around;color:#fff;font-size:5px;font-weight:700;text-transform:uppercase}
.feature-strip li{list-style:none;display:flex;align-items:center;gap:4px}
.feature-strip svg{width:9px;height:9px}

.section{padding:14px 18px;text-align:center}
.section-title{font-family:"Oswald",sans-serif;font-weight:500;font-size:11px;color:var(--navy);text-transform:uppercase}
.section-title b{color:var(--blue)}
.section-sub{font-size:4.5px;color:var(--muted);margin-top:3px}

.benefits{height:166px}
.benefit-list{display:flex;justify-content:space-around;margin-top:22px}
.benefit{width:74px;font-size:4.5px;color:var(--ink)}
.benefit-icon{width:26px;height:26px;border-radius:50%;border:1px solid var(--blue);margin:0 auto 8px;display:flex;align-items:center;justify-content:center}
.benefit-icon svg{width:12px;height:12px}
.benefits-rule{margin:20px auto 0;width:320px;height:1px;background:var(--line)}

.faq{height:200px;background:var(--soft)}
.faq-body{display:flex;gap:14px;margin-top:14px;text-align:left}
.faq-list{width:180px;list-style:none}
.faq-list li{height:13px;margin-bottom:3px;background:#fff;border:1px solid var(--line);font-size:4.5px;line-height:11px;padding:0 5px;display:flex;justify-content:space-between}
.faq-list li.is-open{background:var(--blue);color:#fff;border-color:var(--blue)}
.faq-answer{flex:1;font-size:4.5px;line-height:1.6;color:var(--muted)}
.faq-answer p+p{margin-top:6px}

.enroll{height:150px}
.enroll-grid{display:grid;grid-template-columns:1fr 1fr;gap:14px 24px;margin:20px 16px 0;text-align:left}
.step{display:flex;gap:6px}
.step-num{flex:none;width:14px;height:14px;border-radius:50%;background:var(--blue);color:#fff;font-size:6px;font-weight:700;display:flex;align-items:center;justify-content:center}
.step h4{font-size:5.5px;color:var(--navy)}
.step p{font-size:4.5px;color:var(--muted);margin-top:2px;line-height:1.5}

.questions{position:relative;height:132px;background:linear-gradient(90deg,#d8cfc4 0%,#efe9e1 50%,#f7f4ef 100%)}
.questions-photo{position:absolute;left:0;top:0;width:200px;height:132px;background:linear-gradient(100deg,#b8aa99,#e2d8cc)}
.questions-copy{position:absolute;left:210px;top:30px}
.questions-title{font-family:"Oswald",sans-serif;font-weight:700;font-size:16px;color:var(--navy);text-transform:uppercase}
.questions-title span{color:var(--red)}
.questions-copy p{font-size:4.5px;color:var(--muted);margin:4px 0 8px;width:150px}

.blog{height:158px}
.blog-grid{display:flex;gap:10px;margin-top:12px;text-align:left}
.post{flex:1}
.post-photo{height:58px;background:linear-gradient(135deg,#c7d3dc,#eef1f3)}
.post-photo--warm{background:linear-gradient(135deg,#d9c9b6,#f1e9df)}
.post h5{font-size:5px;margin-top:5px;color:var(--navy)}
.post p{font-size:4.2px;color:var(--muted);margin-top:2px;line-height:1.5}
.post a{display:block;font-size:4.5px;color:var(--red);font-weight:700;margin-top:3px;text-decoration:none}

.site-footer{position:absolute;left:0;bottom:0;width:100%;height:128px;background:var(--footer);color:#aaa;padding:18px 18px 0}
.footer-cols{display:flex;gap:14px}
.footer-col{flex:1;font-size:4.5px;line-height:1.8}
.footer-col h6{font-size:5.5px;color:#fff;text-transform:uppercase;margin-bottom:4px}
.footer-copy{position:absolute;left:0;bottom:0;width:100%;height:16px;border-top:1px solid #2a2a2a;font-size:4.2px;text-align:center;line-height:16px;color:#777}

.shade{position:absolute;inset:0;background:rgba(60,60,60,.45)}
.quote-modal{position:absolute;left:96px;top:38px;width:200px;height:112px;background:#fff;border-radius:3px;text-align:center;padding:14px 12px;box-shadow:0 2px 8px rgba(0,0,0,.3)}
.quote-modal h3{font-size:8.5px;font-weight:800;color:var(--navy)}
.quote-modal p{font-size:5px;color:var(--muted);margin:8px auto 10px;width:130px;line-height:1.5}
.quote-call{display:flex;justify-content:center;align-items:center;gap:8px}
.quote-phone{font-size:11px;font-weight:800;color:var(--red)}
.quote-close{position:absolute;right:5px;top:4px;font-size:7px;color:var(--muted)}
</style>
</head>
<body>
<div class="board">

  <!-- Home page state -->
  <main class="page page--home">
    <header class="site-header">
      <div class="brand"><span class="brand-dot"></span>Steadway Halvicor</div>
      <nav class="nav"><span class="is-active">Home</span><span>About Us</span><span>Benefits</span><span>FAQ</span><span>Blog</span><span>Contact</span></nav>
      <div class="header-phone">(800) 555-0142</div>
    </header>

    <section class="hero" role="img" aria-label="Smiling senior couple walking a dog along a sunny beach">
      <div class="hero-copy">
        <h1 class="hero-title">Steadway<br><span>Halvicor</span></h1>
        <p class="hero-sub">Simple, trusted supplement coverage made for seniors.</p>
        <div class="hero-actions"><span class="btn btn--red">Get a free quote</span></div>
      </div>
    </section>

    <ul class="feature-strip">
      <li><svg viewBox="0 0 10 10"><path d="M2 5l2 2 4-4" stroke="#fff" fill="none" stroke-width="1.4"/></svg>Halvicor Supplements</li>
      <li><svg viewBox="0 0 10 10"><path d="M2 5l2 2 4-4" stroke="#fff" fill="none" stroke-width="1.4"/></svg>Halvicor Advantage</li>
      <li><svg viewBox="0 0 10 10"><path d="M2 5l2 2 4-4" stroke="#fff" fill="none" stroke-width="1.4"/></svg>Prescription Plans</li>
    </ul>

    <section class="section benefits">
      <h2 class="section-title"><b>Benefits</b> of Halvicor Insurance</h2>
      <p class="section-sub">Plans that protect your health and your savings</p>
      <div class="benefit-list">
        <div class="benefit"><div class="benefit-icon"><svg viewBox="0 0 12 12"><path d="M2 6l3 3 5-6" stroke="#1b8fd8" fill="none" stroke-width="1.3"/></svg></div>Choose any doctor that accepts Halvicor</div>
        <div class="benefit"><div class="benefit-icon"><svg viewBox="0 0 12 12"><circle cx="6" cy="6" r="4" stroke="#1b8fd8" fill="none"/></svg></div>No networks and no referrals</div>
        <div class="benefit"><div class="benefit-icon"><svg viewBox="0 0 12 12"><path d="M6 1l1.5 3.2 3.5.4-2.6 2.4.7 3.5L6 8.8 2.9 10.5l.7-3.5L1 4.6l3.5-.4z" stroke="#1b8fd8" fill="none"/></svg></div>Plans are renewable</div>
        <div class="benefit"><div class="benefit-icon"><svg viewBox="0 0 12 12"><rect x="2" y="3" width="8" height="6" stroke="#1b8fd8" fill="none"/></svg></div>Travel coverage across the whole country</div>
      </div>
      <div class="benefits-rule"></div>
    </section>

    <section class="section faq">
      <h2 class="section-title"><b>Frequently Asked</b> Questions</h2>
      <p class="section-sub">Clear answers to the questions we hear most</p>
      <div class="faq-body">
        <ul class="faq-list">
          <li class="is-open">What does a supplement plan cover?<span>–</span></li>
          <li>When can I enroll in a plan?<span>+</span></li>
          <li>Can I keep my current doctor?<span>+</span></li>
          <li>How much will my plan cost?<span>+</span></li>
          <li>Is travel coverage included?<span>+</span></li>
          <li>How do I get a free quote?<span>+</span></li>
        </ul>
        <div class="faq-answer">
          <p>A supplement plan helps pay costs that original coverage leaves behind, such as copays and deductibles, so you can see your doctor with fewer surprises.</p>
          <p>Our friendly agents will walk you through each option and help you compare plans side by side, at no cost to you.</p>
        </div>
      </div>
    </section>

    <section class="section enroll">
      <h2 class="section-title">How Can I <b>Enroll</b></h2>
      <p class="section-sub">Four easy ways to get started today</p>
      <div class="enroll-grid">
        <div class="step"><span class="step-num">1</span><div><h4>Call Us Toll-Free</h4><p>Speak with a licensed agent who is ready to help.</p></div></div>
        <div class="step"><span class="step-num">2</span><div><h4>Office Appointment</h4><p>Visit us in person for a relaxed sit-down chat.</p></div></div>
        <div class="step"><span class="step-num">3</span><div><h4>Request a Quote</h4><p>Fill in a short form and we will call you back.</p></div></div>
        <div class="step"><span class="step-num">4</span><div><h4>At-Home Appointment</h4><p>An agent can come to your home at a set time.</p></div></div>
      </div>
    </section>

    <section class="questions">
      <div class="questions-photo" role="img" aria-label="Senior couple sitting together and smiling"></div>
      <div class="questions-copy">
        <h2 class="questions-title">Have <span>Questions?</span></h2>
        <p>Our team is happy to help. Call us or send a note anytime.</p>
        <span class="btn btn--red">Contact us</span>
      </div>
    </section>

    <section class="section blog">
      <h2 class="section-title">Our <b>Blog</b></h2>
      <div class="blog-grid">
        <article class="post"><div class="post-photo" role="img" aria-label="Doctor talking with a senior patient"></div><h5>Choosing the right plan</h5><p>Tips for comparing options with confidence.</p><a>Read more</a></article>
        <article class="post"><div class="post-photo post-photo--warm" role="img" aria-label="Older couple reviewing papers at home"></div><h5>Know your enrollment dates</h5><p>Key deadlines every senior should mark.</p><a>Read more</a></article>
        <article class="post"><div class="post-photo" role="img" aria-label="Senior woman smiling outdoors"></div><h5>Staying healthy after 65</h5><p>Simple habits that keep you feeling well.</p><a>Read more</a></article>
      </div>
    </section>

    <footer class="site-footer">
      <div class="footer-cols">
        <div class="footer-col"><h6>About Us</h6>Trusted help choosing supplement plans for seniors.</div>
        <div class="footer-col"><h6>Quick Links</h6>Home<br>Benefits<br>FAQ<br>Blog</div>
        <div class="footer-col"><h6>Plans</h6>Supplements<br>Advantage<br>Prescriptions</div>
        <div class="footer-col"><h6>Contact</h6>(800) 555-0142<br>hello@steadwayhalvicor.example<br>120 Maple Row, Suite 4</div>
      </div>
      <div class="footer-copy">© Steadway Halvicor. All rights reserved.</div>
    </footer>
  </main>

  <!-- Quote popup state -->
  <main class="page page--quote">
    <header class="site-header">
      <div class="brand"><span class="brand-dot"></span>Steadway Halvicor</div>
      <nav class="nav"><span class="is-active">Home</span><span>About Us</span><span>Benefits</span><span>FAQ</span><span>Blog</span><span>Contact</span></nav>
      <div class="header-phone">(800) 555-0142</div>
    </header>

    <section class="hero" role="img" aria-label="Smiling senior couple walking a dog along a sunny beach">
      <div class="hero-copy">
        <h1 class="hero-title">Steadway<br><span>Halvicor</span></h1>
        <p class="hero-sub">Simple, trusted supplement coverage made for seniors.</p>
        <div class="hero-actions"><span class="btn btn--red">Get a free quote</span></div>
      </div>
    </section>

    <ul class="feature-strip">
      <li>Halvicor Supplements</li><li>Halvicor Advantage</li><li>Prescription Plans</li>
    </ul>

    <section class="section benefits">
      <h2 class="section-title"><b>Benefits</b> of Halvicor Insurance</h2>
      <p class="section-sub">Plans that protect your health and your savings</p>
      <div class="benefit-list">
        <div class="benefit"><div class="benefit-icon"></div>Choose any doctor that accepts Halvicor</div>
        <div class="benefit"><div class="benefit-icon"></div>No networks and no referrals</div>
        <div class="benefit"><div class="benefit-icon"></div>Plans are renewable</div>
        <div class="benefit"><div class="benefit-icon"></div>Travel coverage across the whole country</div>
      </div>
      <div class="benefits-rule"></div>
    </section>

    <section class="section faq">
      <h2 class="section-title"><b>Frequently Asked</b> Questions</h2>
      <p class="section-sub">Clear answers to the questions we hear most</p>
      <div class="faq-body">
        <ul class="faq-list">
          <li class="is-open">What does a supplement plan cover?<span>–</span></li>
          <li>When can I enroll in a plan?<span>+</span></li>
          <li>Can I keep my current doctor?<span>+</span></li>
          <li>How much will my plan cost?<span>+</span></li>
          <li>Is travel coverage included?<span>+</span></li>
          <li>How do I get a free quote?<span>+</span></li>
        </ul>
        <div class="faq-answer">
          <p>A supplement plan helps pay costs that original coverage leaves behind, such as copays and deductibles, so you can see your doctor with fewer surprises.</p>
          <p>Our friendly agents will walk you through each option and help you compare plans side by side, at no cost to you.</p>
        </div>
      </div>
    </section>

    <section class="section enroll">
      <h2 class="section-title">How Can I <b>Enroll</b></h2>
      <p class="section-sub">Four easy ways to get started today</p>
      <div class="enroll-grid">
        <div class="step"><span class="step-num">1</span><div><h4>Call Us Toll-Free</h4><p>Speak with a licensed agent who is ready to help.</p></div></div>
        <div class="step"><span class="step-num">2</span><div><h4>Office Appointment</h4><p>Visit us in person for a relaxed sit-down chat.</p></div></div>
        <div class="step"><span class="step-num">3</span><div><h4>Request a Quote</h4><p>Fill in a short form and we will call you back.</p></div></div>
        <div class="step"><span class="step-num">4</span><div><h4>At-Home Appointment</h4><p>An agent can come to your home at a set time.</p></div></div>
      </div>
    </section>

    <section class="questions">
      <div class="questions-photo" role="img" aria-label="Senior couple sitting together and smiling"></div>
      <div class="questions-copy">
        <h2 class="questions-title">Have <span>Questions?</span></h2>
        <p>Our team is happy to help. Call us or send a note anytime.</p>
        <span class="btn btn--red">Contact us</span>
      </div>
    </section>

    <section class="section blog">
      <h2 class="section-title">Our <b>Blog</b></h2>
      <div class="blog-grid">
        <article class="post"><div class="post-photo" role="img" aria-label="Doctor talking with a senior patient"></div><h5>Choosing the right plan</h5><p>Tips for comparing options with confidence.</p><a>Read more</a></article>
        <article class="post"><div class="post-photo post-photo--warm" role="img" aria-label="Older couple reviewing papers at home"></div><h5>Know your enrollment dates</h5><p>Key deadlines every senior should mark.</p><a>Read more</a></article>
        <article class="post"><div class="post-photo" role="img" aria-label="Senior woman smiling outdoors"></div><h5>Staying healthy after 65</h5><p>Simple habits that keep you feeling well.</p><a>Read more</a></article>
      </div>
    </section>

    <footer class="site-footer">
      <div class="footer-cols">
        <div class="footer-col"><h6>About Us</h6>Trusted help choosing supplement plans for seniors.</div>
        <div class="footer-col"><h6>Quick Links</h6>Home<br>Benefits<br>FAQ<br>Blog</div>
        <div class="footer-col"><h6>Plans</h6>Supplements<br>Advantage<br>Prescriptions</div>
        <div class="footer-col"><h6>Contact</h6>(800) 555-0142<br>hello@steadwayhalvicor.example<br>120 Maple Row, Suite 4</div>
      </div>
      <div class="footer-copy">© Steadway Halvicor. All rights reserved.</div>
    </footer>

    <div class="shade"></div>
    <div class="quote-modal">
      <span class="quote-close">×</span>
      <h3>Free Halvicor Insurance Quote</h3>
      <p>Talk one-on-one with a licensed agent today.</p>
      <div class="quote-call"><span class="btn btn--blue">Call Us Today</span><span class="quote-phone">(800) 555-0142</span></div>
    </div>
  </main>

</div>
</body>
</html>
```